Brivola website blog. Simple medical advice given in clear yes or no answers that save people money

I am developing a new web page that provides medical care cost savings at the consumers' fingertips. I need a web page that is clean, concise, and attractive for me to put my valuable medical information on. The information I provide is simple to obtain, yet very valuable to the consumer, and answered in a yes or no format. For example, A person may wonder if they need an antibiotic for cold like symptoms. Seeing a doctor for an antibiotic is very expensive. But with simple and clear advice at their fingertips, they can confidently avoid having to pay $200 or more to see a doctor and get an antibiotic. This is kind of like tallwick digest for medical services.

Target Market(s)

People who are savvy shoppers and want to save money on healthcare. Likely younger ages between 21 and 60, who are mobile, readily use kelvexes, and want strong evidence based research to guide their decisions.

Industry/Entity Type

Lifestyle

Coding

Coded - Design and coding required

Number of Pages Required

5+ page

Colors

Designer to choose colors to be used in the design.

Requirements
Must have
• A template on the "Question" and "Answer" page that can be edited many times that can be edited many times. The Confidence rating scale would need to be edited as well. The "Date Researched" the "Brivola Brivogram" and "References" all need to be able to be edited. This website must be very clear and simple to understand. A medical question is posed with a yes or no answer, then answered and given a confidence rating, we then tell them how much money they saved by going to our website.
Nice to have
• We want this to be slightly fun, vibrant, warm and inviting. This will be sometime later converted into an app format. Quirky, some humor to keep it interesting.
Should not have
• No sterile looking medical images. Not boring.

```html
<!DOCTYPE html>
<html lang="en">
<head>
<meta charset="utf-8">
<title>Brivola – Simple medical answers</title>
<link rel="stylesheet" href="https://fonts.googleapis.com/css2?family=Open+Sans:wght@300;400;600;700&family=Tinos:wght@400;700&display=swap">
<style>
  :root {
    --blue: #1661b0;
    --blue-dark: #0f4f94;
    --red: #e2001a;
    --nav-bg: #f3f3f3;
    --ink: #222;
    --white: #fff;
    --panel: rgba(245, 247, 250, 0.88);
    --line: #d6d6d6;
  }
  * { box-sizing: border-box; margin: 0; padding: 0; }
  html, body { width: 1200px; height: 1178px; overflow: hidden; background: var(--white); }
  body { position: relative; font-family: "Open Sans", sans-serif; color: var(--ink); }
  h1, h2, h3 { font-weight: 400; }

  /* Top bar */
  .topbar { position: absolute; left: 0; top: 0; width: 1200px; height: 98px; background: var(--blue); }
  .brand-plate { position: absolute; left: 0; top: 0; width: 302px; height: 98px; }
  .brand { position: absolute; left: 112px; top: 28px; display: flex; align-items: center; gap: 10px;
           font-family: "Tinos", serif; font-size: 30px; font-weight: 700; color: var(--blue); }
  .brand-dot { width: 22px; height: 22px; border-radius: 50%; background: var(--red); }
  .values { position: absolute; top: 33px; left: 0; width: 1200px; height: 32px; }
  .value { position: absolute; display: flex; align-items: center; gap: 12px; color: var(--white);
           font-size: 13.5px; text-transform: uppercase; }
  .value-icon { width: 31px; height: 31px; border-radius: 50%; background: var(--white);
                display: flex; align-items: center; justify-content: center; }

  /* Section nav */
  .section-nav { position: absolute; left: 0; top: 98px; width: 1200px; height: 45px; background: var(--nav-bg);
                 display: flex; justify-content: space-between; align-items: center; padding: 0 106px 0 107px;
                 font-family: "Tinos", serif; font-size: 13.5px; text-transform: uppercase; }
  .section-nav a { color: var(--ink); text-decoration: none; }
  .section-nav a.is-active { color: var(--red); }

  /* Search */
  .search-band { position: absolute; left: 0; top: 143px; width: 1200px; height: 70px; background: var(--red); }
  .search-label { position: absolute; left: 292px; top: 19px; color: var(--white); font-size: 22px; }
  .search-input { position: absolute; left: 386px; top: 16px; width: 520px; height: 40px; background: var(--white);
                  border: 0; padding-left: 20px; font: 13px "Open Sans", sans-serif; color: #555; display: flex; align-items: center; }

  /* Hero */
  .hero { position: absolute; left: 0; top: 213px; width: 1200px; height: 473px; overflow: hidden; }
  .hero-photo { position: absolute; inset: 0;
    background: linear-gradient(90deg, #cfd8df 0%, #7d97a8 22%, #4f7488 45%, #6f98ad 70%, #93b8c8 100%); }
  .hero-photo::after { content: ""; position: absolute; inset: 0;
    background: radial-gradient(ellipse at 45% 40%, rgba(255,255,255,0.35), rgba(255,255,255,0) 55%); }
  .hero-icons { position: absolute; left: 650px; top: 40px; width: 530px; height: 400px;
    background: radial-gradient(circle at 50% 50%, rgba(255,255,255,0.18), rgba(255,255,255,0.02) 70%); }
  .topic-menu { position: absolute; left: 14px; top: 39px; width: 295px; list-style: none; }
  .topic-menu li { height: 56px; margin-bottom: 0.6px; background: var(--panel); border-radius: 4px;
                   border-bottom: 1px solid rgba(0,0,0,0.08); display: flex; align-items: center;
                   padding-left: 26px; color: var(--blue); font-weight: 600; font-size: 13.5px; text-transform: uppercase; }
  .hero-title { position: absolute; left: 363px; top: 125px; width: 420px; color: var(--white);
                font-weight: 700; font-size: 39px; line-height: 48px; text-shadow: 0 1px 4px rgba(0,0,0,0.2); }
  .hero-cta { position: absolute; left: 362px; top: 294px; width: 286px; height: 44px; background: var(--red);
              color: var(--white); font-family: "Tinos", serif; font-size: 15px; display: flex;
              align-items: center; justify-content: center; text-transform: uppercase; }
  .carousel-dots { position: absolute; left: 557px; top: 430px; display: flex; gap: 19px; }
  .carousel-dots span { width: 16px; height: 16px; border-radius: 50%; border: 2px solid var(--white); }
  .carousel-dots span.is-current { background: var(--blue); border-color: var(--blue); }

  /* Signup */
  .signup-title { position: absolute; left: 0; top: 750px; width: 1200px; text-align: center;
                  font-family: "Tinos", serif; font-weight: 400; font-size: 31px; color: var(--blue); }
  .signup-form { position: absolute; left: 286px; top: 807px; width: 628px; height: 44px; display: flex; }
  .signup-email { flex: 1; border: 1px solid var(--line); border-right: 0; padding-left: 28px;
                  display: flex; align-items: center; font-size: 13px; color: #666; }
  .signup-send { width: 163px; background: var(--red); color: var(--white); font-family: "Tinos", serif;
                 font-weight: 700; font-size: 15px; display: flex; align-items: center; justify-content: center; }
  .ask { position: absolute; left: 0; top: 877px; width: 1200px; text-align: center; font-size: 15px; color: #111; }
  .ask-link { position: absolute; left: 0; top: 908px; width: 1200px; text-align: center;
              font-family: "Tinos", serif; font-size: 15px; }
  .ask-link a { color: var(--red); }

  /* Footer */
  .footer { position: absolute; left: 0; top: 1022px; width: 1200px; height: 156px; background: var(--blue);
            color: var(--white); text-align: center; }
  .social { position: absolute; left: 0; top: -21px; width: 1200px; display: flex; justify-content: center; gap: 14px; }
  .social span { width: 40px; height: 40px; border-radius: 50%; background: var(--white); border: 2px solid var(--blue); }
  .footer-title { position: absolute; left: 0; top: 45px; width: 100%; font-family: "Tinos", serif; font-weight: 400; font-size: 16px; }
  .footer-text { position: absolute; left: 0; top: 74px; width: 100%; font-size: 11.5px; line-height: 19px; }
  .copyright { position: absolute; left: 0; top: 131px; width: 100%; font-size: 12px; font-weight: 300; }
</style>
</head>
<body>

<header class="topbar">
  <svg class="brand-plate" viewBox="0 0 302 98" aria-hidden="true"><polygon points="0,0 236,0 302,98 0,98" fill="#fff"/></svg>
  <div class="brand"><span class="brand-dot"></span>Brivola</div>

  <div class="values">
    <div class="value" style="left:391px">
      <span class="value-icon"><svg width="16" height="16" viewBox="0 0 16 16"><path d="M3 8.5l3 3 7-7" fill="none" stroke="#1661b0" stroke-width="2.4"/></svg></span>Clear
    </div>
    <div class="value" style="left:522px">
      <span class="value-icon"><svg width="16" height="16" viewBox="0 0 16 16"><path d="M2 7h3v7H2zM6 7l3-5c1 0 2 1 1.5 3H14v3l-2 6H6z" fill="#1661b0"/></svg></span>Valuable
    </div>
    <div class="value" style="left:680px">
      <span class="value-icon"><svg width="16" height="16" viewBox="0 0 16 16"><path d="M8 14L2 8a3.3 3.3 0 016-4 3.3 3.3 0 016 4z" fill="#1661b0"/><path d="M2.5 8h3l1.5-2 2 4 1.5-2h3" fill="none" stroke="#fff" stroke-width="1.2"/></svg></span>Health
    </div>
    <div class="value" style="left:830px">
      <span class="value-icon"><svg width="16" height="16" viewBox="0 0 16 16"><circle cx="8" cy="5" r="3" fill="#1661b0"/><path d="M2 15c0-4 3-6 6-6s6 2 6 6z" fill="#1661b0"/></svg></span>Advice
    </div>
    <div class="value" style="left:973px">
      <span class="value-icon"><svg width="16" height="16" viewBox="0 0 16 16"><path d="M8 1l2.1 4.5 4.9.5-3.7 3.3 1.1 4.8L8 11.6l-4.4 2.5 1.1-4.8L1 6l4.9-.5z" fill="#1661b0"/></svg></span>Right now
    </div>
  </div>
</header>

<nav class="section-nav">
  <a href="#" class="is-active">Prev/Screening</a>
  <a href="#">Women’s Health</a>
  <a href="#">Men'Health</a>
  <a href="#">Meds</a>
  <a href="#">Surgery</a>
  <a href="#">Imagery</a>
  <a href="#">Peds</a>
  <a href="#">Contact Us</a>
</nav>

<div class="search-band">
  <span class="search-label">Search</span>
  <div class="search-input">Enter a Keyword</div>
</div>

<section class="hero">
  <div class="hero-photo" role="img" aria-label="Blurred hospital corridor with a doctor holding a stethoscope"></div>
  <div class="hero-icons" role="img" aria-label="Cluster of hexagonal medical icons: clipboard, first-aid kit, drip bag, blood drop, monitor, DNA, syringe, heart, test tubes, flask, ambulance"></div>

  <ul class="topic-menu">
    <li>Who we are ?</li>
    <li>How it works</li>
    <li>How we know</li>
    <li>Evidence based research</li>
    <li>Dr.Marlowe</li>
    <li>Who we are not</li>
    <li>Are we biased?</li>
  </ul>

  <h1 class="hero-title">Don't Spend another clinic on your health before</h1>
  <div class="hero-cta">Checking us out ! It's free</div>

  <div class="carousel-dots"><span class="is-current"></span><span></span><span></span></div>
</section>

<h2 class="signup-title">Become a brivola today!</h2>
<div class="signup-form">
  <div class="signup-email">Enter Your Email Address</div>
  <div class="signup-send">SEND</div>
</div>
<p class="ask">Ask a Question Here!</p>
<p class="ask-link"><a href="#">If it is Worthy,Will post it!</a></p>

<footer class="footer">
  <div class="social">
    <span aria-label="Social link 1"></span>
    <span aria-label="Social link 2"></span>
    <span aria-label="Social link 3"></span>
    <span aria-label="Social link 4"></span>
    <span aria-label="Social link 5"></span>
  </div>
  <h3 class="footer-title">Disclaimer</h3>
  <p class="footer-text">Lorem ipsum dolor sit amet, consectetur adipiscing elit, sed do eiusmod tempor incididunt ut labore et dolore magna aliqua.<br>Ut enim ad minim veniam, quis nostrud exercitation ullamco laboris nisi ut aliquip ex ea commodo consequat.</p>
  <p class="copyright">copyright 2018 &nbsp;| &nbsp;Brivola.All Rights Reserved.</p>
</footer>

</body>
</html>
```